BrovaLT BIZ Card, email signature & Stationary

Professional business cards, email signatures and ms word letterhead

Target Market(s)

business owners

Industry/Entity Type

cloud hosting

Contact Information for Business Card

name title office phone number , direct line, fax email address web site

Font styles to use
Other font styles liked:
• something that compliments font in logo

```html
<!DOCTYPE html>
<html lang="en">
<head>
<meta charset="utf-8">
<title>BrovaLT Business Card</title>
<link href="https://fonts.googleapis.com/css2?family=Open+Sans:wght@300;400;600&display=swap" rel="stylesheet">
<style>
  :root {
    --bg: #e4e4e2;
    --paper: #f7f7f5;
    --ink: #1c1c1c;
    --red: #dd2229;
    --black-card: #161616;
    --logo-grey: #a3a3a3;
    --white: #ffffff;
  }
  * { box-sizing: border-box; margin: 0; padding: 0; }
  html, body { width: 1200px; height: 801px; overflow: hidden; }
  body {
    background: var(--bg);
    font-family: "Open Sans", Arial, sans-serif;
    position: relative;
  }
  .card {
    position: absolute;
    top: 263px;
    width: 480px;
    height: 274px;
    overflow: hidden;
    box-shadow: 0 2px 6px rgba(0,0,0,0.18);
  }
  .card--front { left: 90px; background: var(--paper); color: var(--ink); }
  .card--back { left: 630px; background: var(--black-card); }

  .brand-name {
    position: absolute;
    left: 150px;
    top: 22px;
    font-size: 66px;
    font-weight: 300;
    color: var(--red);
    letter-spacing: 1px;
    line-height: 1;
  }
  .divider {
    position: absolute;
    left: 150px;
    top: 112px;
    width: 312px;
    height: 1px;
    background: var(--ink);
  }
  .person { position: absolute; left: 26px; top: 128px; }
  .person__name {
    font-size: 15px;
    font-weight: 600;
    color: var(--red);
    letter-spacing: 0.3px;
  }
  .person__title { font-size: 12px; font-weight: 400; margin-top: 1px; }
  .person__rule { width: 138px; height: 1px; background: var(--red); margin: 6px 0 7px; }
  .contact-list { list-style: none; font-size: 11px; line-height: 15px; }
  .contact-list li { display: flex; align-items: center; gap: 6px; }
  .contact-list svg { width: 10px; height: 10px; flex: none; }

  .office-address {
    position: absolute;
    left: 296px;
    top: 148px;
    font-size: 12px;
    line-height: 16px;
  }
  .band { position: absolute; left: 0; bottom: 0; width: 480px; height: 28px; }
  .band__address {
    position: absolute;
    left: 26px;
    bottom: 7px;
    font-size: 11px;
    color: var(--white);
  }
  .band__web {
    position: absolute;
    right: 26px;
    bottom: 7px;
    font-size: 11px;
    color: var(--white);
  }
  .back-brand {
    position: absolute;
    left: 0; right: 0;
    top: 100px;
    text-align: center;
    font-size: 60px;
    font-weight: 300;
    color: var(--logo-grey);
    letter-spacing: 1px;
    line-height: 1;
  }
</style>
</head>
<body>
  <section class="card card--front">
    <div class="brand-name">BrovaLT</div>
    <div class="divider"></div>

    <div class="person">
      <div class="person__name">MARCUS ELLERY</div>
      <div class="person__title">Managing Director</div>
      <div class="person__rule"></div>
      <ul class="contact-list">
        <li><svg viewBox="0 0 10 10"><circle cx="5" cy="5" r="5" fill="#dd2229"/><path d="M3 3.2c0 2 1.8 3.8 3.8 3.8l.6-.9-1-.6-.5.5c-.8-.4-1.3-.9-1.7-1.7l.5-.5-.6-1z" fill="#fff"/></svg>(214) 555-0142</li>
        <li><svg viewBox="0 0 10 10"><circle cx="5" cy="5" r="5" fill="#dd2229"/><rect x="3.5" y="2.5" width="3" height="5" rx="0.5" fill="#fff"/></svg>(000) 000-0000</li>
        <li><svg viewBox="0 0 10 10"><circle cx="5" cy="5" r="5" fill="#dd2229"/><rect x="2.5" y="4" width="5" height="3" fill="#fff"/><rect x="3.5" y="2.5" width="3" height="1.5" fill="#fff"/></svg>(000) 000-0000</li>
        <li><svg viewBox="0 0 10 10"><circle cx="5" cy="5" r="5" fill="#dd2229"/><rect x="2.5" y="3.2" width="5" height="3.6" fill="#fff"/><path d="M2.5 3.2L5 5.2 7.5 3.2" stroke="#dd2229" stroke-width="0.6" fill="none"/></svg>info@brovalt.com</li>
      </ul>
    </div>

    <div class="office-address">480 Harbor Lane,<br>Suite 210, Austin, TX 78701</div>

    <svg class="band" viewBox="0 0 480 28" aria-hidden="true">
      <polygon points="0,0 316,0 306,28 0,28" fill="#161616"/>
      <polygon points="322,0 480,0 480,28 312,28" fill="#dd2229"/>
    </svg>
    <div class="band__address">480 Harbor Lane, Suite 210, Austin, TX 78701</div>
    <div class="band__web">www.brovalt.com</div>
  </section>

  <section class="card card--back">
    <div class="back-brand">BrovaLT</div>
  </section>
</body>
</html>
```